Business Cards

We are wanting business cards created using previous design #36167008 as a starting point.
Info needed on front side:
Employee Name
Title
Email
Phone Number

Info needed on back side: (these are our product lines)
Frac Valves Fishing
Flowback Thru-Tubing
Torque & Test KMVB

please see changes

```html
<!DOCTYPE html>
<html lang="en">
<head>
<meta charset="utf-8">
<title>Kestrel Downhole Tools — Business Cards</title>
<link rel="stylesheet" href="https://fonts.googleapis.com/css2?family=Michroma&family=Poppins:wght@400;500;600;800&display=swap">
<style>
  :root {
    --backdrop: #1c1c1d;
    --card: #151516;
    --gold: #d8b856;
    --gold-soft: #a88f55;
    --white: #f4f1ea;
    --faint: rgba(168, 143, 85, 0.10);
  }
  * { box-sizing: border-box; margin: 0; padding: 0; }
  html, body { width: 1200px; height: 1200px; overflow: hidden; background: var(--backdrop); }
  body { font-family: "Poppins", sans-serif; color: var(--white); }

  .sheet {
    width: 1200px; height: 1200px;
    display: flex; flex-direction: column; align-items: center; justify-content: center;
    gap: 60px;
  }
  .card {
    position: relative;
    width: 900px; height: 514px;
    background: var(--card);
    box-shadow: 0 18px 40px rgba(0,0,0,0.55);
    overflow: hidden;
  }

  /* brand block */
  .brand { position: absolute; text-align: left; }
  .brand-mark {
    display: block;
    border: 5px solid var(--gold-soft);
    border-radius: 50%;
  }
  .brand-name {
    font-family: "Poppins", sans-serif;
    font-weight: 800;
    color: var(--gold);
    letter-spacing: 0.02em;
    line-height: 1;
    white-space: nowrap;
  }
  .brand-name .brand-sub {
    display: block;
    font-size: 0.26em;
    letter-spacing: 0.06em;
    margin-top: 8px;
  }

  .divider {
    position: absolute;
    width: 2px;
    background: linear-gradient(to bottom, transparent, var(--gold) 25%, var(--gold) 75%, transparent);
  }

  /* front */
  .front .brand { left: 110px; top: 120px; width: 380px; text-align: center; }
  .front .brand-mark { width: 130px; height: 130px; margin: 0 auto 22px; }
  .front .brand-name { font-size: 62px; }
  .front .divider { left: 525px; top: 120px; height: 250px; }

  .person { position: absolute; left: 565px; top: 140px; width: 310px; }
  .person-name {
    font-family: "Michroma", sans-serif;
    color: var(--gold);
    font-size: 24px;
    letter-spacing: 0.04em;
    white-space: nowrap;
  }
  .person-title {
    font-family: "Michroma", sans-serif;
    font-size: 13px;
    letter-spacing: 0.12em;
    padding-bottom: 10px;
    width: 160px;
    border-bottom: 1px solid var(--white);
  }
  .contacts { list-style: none; margin-top: 40px; }
  .contacts li {
    display: flex; align-items: center; gap: 12px;
    font-size: 18px; letter-spacing: 0.02em; line-height: 1.6;
    white-space: nowrap;
  }
  .icon {
    flex: none;
    width: 22px; height: 22px; border-radius: 50%;
    background: var(--gold);
    display: inline-flex; align-items: center; justify-content: center;
  }
  .icon svg { width: 13px; height: 13px; }

  /* back */
  .back .deco {
    position: absolute; left: 250px; top: 50px;
    width: 420px; height: 420px;
    border: 28px solid var(--faint);
    border-radius: 50%;
  }
  .back .brand { left: 70px; top: 185px; }
  .back .brand-name { font-size: 64px; }
  .back .divider { left: 405px; top: 160px; height: 190px; }

  .product-lines {
    position: absolute; left: 440px; top: 186px; width: 430px;
    list-style: none;
    display: grid; grid-template-columns: 1fr 1fr; column-gap: 20px;
  }
  .product-lines li {
    position: relative; padding-left: 32px;
    font-size: 23px; font-weight: 500; letter-spacing: 0.02em; line-height: 1.75;
    white-space: nowrap;
  }
  .product-lines li::before {
    content: ""; position: absolute; left: 0; top: 50%;
    width: 13px; height: 13px; margin-top: -6.5px;
    border-radius: 50%; background: var(--gold);
  }
  .locations {
    position: absolute; left: 0; right: 0; bottom: 70px;
    text-align: center; font-size: 30px; letter-spacing: 0.04em;
  }
</style>
</head>
<body>
<main class="sheet">

  <section class="card front" aria-label="Card front">
    <div class="brand">
      <span class="brand-mark" aria-hidden="true"></span>
      <div class="brand-name">KESTREL<span class="brand-sub">DOWNHOLE TOOLS, LLC.</span></div>
    </div>
    <span class="divider" aria-hidden="true"></span>
    <div class="person">
      <h1 class="person-name">DANIEL REYES</h1>
      <p class="person-title">DIRECTOR</p>
      <ul class="contacts">
        <li>
          <span class="icon"><svg viewBox="0 0 12 12"><rect x="3" y="1" width="6" height="10" rx="1" fill="none" stroke="#151516" stroke-width="1.4"/></svg></span>
          (555) 013-2468
        </li>
        <li>
          <span class="icon"><svg viewBox="0 0 12 12"><path d="M3 1.5 L5 4 L4 5.2 Q5 7.5 6.8 8 L8 7 L10.5 9 L9.3 10.5 Q4 10 1.5 3 Z" fill="#151516"/></svg></span>
          (555) 013-2468
        </li>
        <li>
          <span class="icon"><svg viewBox="0 0 12 12"><rect x="1.5" y="3" width="9" height="6.5" fill="none" stroke="#151516" stroke-width="1.3"/><path d="M1.5 3 L6 7 L10.5 3" fill="none" stroke="#151516" stroke-width="1.3"/></svg></span>
          info@kestreltools.example
        </li>
      </ul>
    </div>
  </section>

  <section class="card back" aria-label="Card back">
    <span class="deco" aria-hidden="true"></span>
    <div class="brand">
      <div class="brand-name">KESTREL<span class="brand-sub">DOWNHOLE TOOLS, LLC.</span></div>
    </div>
    <span class="divider" aria-hidden="true"></span>
    <ul class="product-lines">
      <li>Frac Valves</li>
      <li>Fishing</li>
      <li>Flowback</li>
      <li>Thru-Tubing</li>
      <li>Torque &amp; Test</li>
      <li>KMVB</li>
    </ul>
    <p class="locations">Ridgeport - Alder Springs</p>
  </section>

</main>
</body>
</html>
```